Inefficiency of Commercial Realestate (leasing, negotiation, etc)

I'm working on a powerpoint deck and I need some help making it more graphical. The powerpoint outlines the problems "problems" in the commercial real estate industry now and how our software makes the process easier. I'm trying to visualize the inefficiencies of brokers emailing back and forth a Microsoft word document then taking the negotiated document which is just a letter of intent and having to convert it into an abstract and a lease. When visualizing this conversion, I want to show that it's very tedious and prone to human error.
Problems to visualize:
Emailing a .doc file back and forth is frustrating and can take forever. Problems such as am I editing the right version, did they do it in a compatible version of word, etc
Once we've negotiated the LOI, manually converting it to a Lease and abstract takes time and is prone to human error. Additionally, if I want to hire a lawyer to do it it is expensive ($2-3k)
All this work is not reportable to my manager. If he wants to know what I've been spending my time on, I have to create an activity document and manually type it all out.
These documents are all over the place and not in one central location.
In addition to these visualizations, helping improve the overall look and feel and template of the attached presentation.

```html
<!DOCTYPE html>
<html lang="en">
<head>
<meta charset="utf-8">
<title>The Problem</title>
<link rel="stylesheet" href="https://fonts.googleapis.com/css2?family=Arimo:wght@400&display=swap">
<style>
  :root {
    --header-dark: #3f3e3c;
    --header-line: #5c5b58;
    --accent: #f26b1d;
    --box-fill-top: #fcd9b8;
    --box-fill-bottom: #f6b47b;
    --box-border: #e8782f;
    --ink: #161616;
    --icon: #1c1c1c;
    --paper: #ffffff;
  }
  * { box-sizing: border-box; margin: 0; padding: 0; }
  html, body { width: 1200px; height: 900px; overflow: hidden; background: var(--paper); }
  body { font-family: "Arimo", "Helvetica Neue", Arial, sans-serif; color: var(--ink); }

  .slide { position: relative; width: 1200px; height: 900px; background: var(--paper); }

  .slide-header {
    position: absolute; left: 0; top: 0; width: 1200px; height: 252px;
    background:
      repeating-linear-gradient(-45deg, var(--header-line) 0 2px, var(--header-dark) 2px 6px);
  }
  .header-rule {
    position: absolute; left: 0; top: 252px; width: 1200px; height: 18px;
    background: var(--accent);
    box-shadow: 0 3px 5px rgba(0,0,0,0.25);
  }
  .slide-title {
    position: absolute; left: 0; top: 66px; width: 1200px; text-align: center;
    color: #fff; font-weight: 400; font-size: 114px; line-height: 1;
    text-shadow: 3px 3px 4px rgba(0,0,0,0.55);
  }

  .lead {
    position: absolute; left: 0; top: 297px; width: 1192px; text-align: center;
    font-size: 30px; line-height: 40px;
  }

  .flow-lines { position: absolute; left: 0; top: 0; width: 1200px; height: 900px; }

  .step {
    position: absolute; display: flex; align-items: center;
    background:
      repeating-linear-gradient(-45deg, rgba(255,255,255,0.28) 0 1px, transparent 1px 5px),
      linear-gradient(180deg, var(--box-fill-top), var(--box-fill-bottom));
    border: 2px solid var(--box-border); border-radius: 9px;
    box-shadow: 2px 3px 5px rgba(0,0,0,0.25);
    font-size: 22px; line-height: 29px; white-space: nowrap;
  }
  .step-icon { position: absolute; }
  .step-note { display: block; font-size: 15px; line-height: 20px; }

  .step--gather   { left: 107px; top: 403px; width: 222px; height: 95px; padding-left: 66px; }
  .step--draft    { left: 357px; top: 403px; width: 226px; height: 95px; padding-left: 120px; }
  .step--send     { left: 610px; top: 403px; width: 223px; height: 95px; padding-left: 86px; }
  .step--exchange { left: 860px; top: 403px; width: 230px; height: 95px; padding-left: 102px; }
  .step--rounds   { left: 335px; top: 517px; width: 555px; height: 120px; padding-left: 126px; }
  .step--agree    { left: 482px; top: 658px; width: 245px; height: 52px; padding-left: 59px; }
  .step--lawyer   { left: 482px; top: 728px; width: 243px; height: 129px; padding-left: 56px; padding-top: 4px; }

  .step--gather .step-icon   { left: 14px; top: 28px; }
  .step--draft .step-icon    { left: 16px; top: 20px; }
  .step--send .step-icon     { left: 22px; top: 26px; }
  .step--exchange .step-icon { left: 18px; top: 18px; }
  .step--rounds .clock       { left: 12px; top: 8px; }
  .step--rounds .pages       { left: 60px; top: 58px; }
  .step--agree .step-icon    { left: 14px; top: 10px; }

  .figure-placeholder {
    position: absolute; left: 14px; top: 28px; width: 30px; height: 78px;
    border-radius: 12px 12px 4px 4px; background: #1e1e1e;
  }
</style>
</head>
<body>
<main class="slide">
  <div class="slide-header"></div>
  <div class="header-rule"></div>
  <h1 class="slide-title">The Problem</h1>

  <p class="lead">Creating Documents is tedious, prone to<br>human error, and often times redundant work.</p>

  <svg class="flow-lines" viewBox="0 0 1200 900" aria-hidden="true">
    <g stroke="var(--box-border)" stroke-width="3" fill="none">
      <line x1="329" y1="450" x2="357" y2="450"/>
      <line x1="583" y1="450" x2="610" y2="450"/>
      <line x1="833" y1="450" x2="860" y2="450"/>
      <line x1="597" y1="450" x2="597" y2="517"/>
      <line x1="597" y1="637" x2="597" y2="658"/>
      <line x1="597" y1="710" x2="597" y2="728"/>
    </g>
  </svg>

  <div class="step step--gather">
    <svg class="step-icon" width="44" height="36" viewBox="0 0 44 36" aria-hidden="true">
      <path d="M2 4 h14 l4 4 h22 v26 h-40 z" fill="var(--icon)"/>
    </svg>
    <span>broker<br>gathers core<br>characteristics</span>
  </div>

  <div class="step step--draft">
    <svg class="step-icon" width="54" height="52" viewBox="0 0 54 52" aria-hidden="true">
      <g fill="none" stroke="var(--icon)" stroke-width="2.5" stroke-linejoin="round">
        <path d="M8 34 l4-10 L34 2 l6 6 L18 30 z"/>
        <line x1="12" y1="24" x2="18" y2="30"/>
        <path d="M20 38 q10-8 20-4 l10 4 v10 h-18 q-8 0-12-4"/>
      </g>
    </svg>
    <span>broker<br>creates<br>LOI</span>
  </div>

  <div class="step step--send">
    <svg class="step-icon" width="46" height="40" viewBox="0 0 46 40" aria-hidden="true">
      <g fill="none" stroke="var(--icon)" stroke-width="2.5">
        <rect x="6" y="3" width="34" height="22" rx="2"/>
        <path d="M2 34 h42 l-4-6 h-34 z"/>
      </g>
    </svg>
    <span>emails<br>LOI to<br>other broker</span>
  </div>

  <div class="step step--exchange">
    <svg class="step-icon" width="66" height="56" viewBox="0 0 66 56" aria-hidden="true">
      <g fill="none" stroke="var(--icon)" stroke-width="2.2">
        <rect x="24" y="2" width="18" height="13"/>
        <rect x="2" y="34" width="18" height="13"/>
        <rect x="46" y="34" width="18" height="13"/>
        <path d="M33 15 v9 M11 34 v-8 h44 v8"/>
        <path d="M25 41 h16 M25 41 l4-3 M25 41 l4 3 M41 41 l-4-3 M41 41 l-4 3"/>
      </g>
    </svg>
    <span>they email<br>back and<br>forth</span>
  </div>

  <div class="step step--rounds">
    <svg class="step-icon clock" width="50" height="50" viewBox="0 0 50 50" aria-hidden="true">
      <g fill="none" stroke="var(--icon)" stroke-width="2.5">
        <circle cx="25" cy="25" r="22"/>
        <path d="M25 10 v15 l9 12"/>
      </g>
    </svg>
    <svg class="step-icon pages" width="42" height="44" viewBox="0 0 42 44" aria-hidden="true">
      <g fill="#fff" stroke="var(--icon)" stroke-width="2">
        <rect x="16" y="2" width="22" height="28"/>
        <rect x="10" y="8" width="22" height="28"/>
        <rect x="4" y="14" width="22" height="28"/>
      </g>
    </svg>
    <span>with each round of negotiation it takes<br>time and generates more and more<br>individual documents to keep track of</span>
  </div>

  <div class="step step--agree">
    <svg class="step-icon" width="30" height="30" viewBox="0 0 30 30" aria-hidden="true">
      <path d="M3 13 h6 v14 h-6 z M11 13 l5-10 q3 0 3 4 l-1 5 h8 q2 1 1 4 l-3 10 q-1 2-3 2 h-10 z" fill="none" stroke="var(--icon)" stroke-width="2" stroke-linejoin="round"/>
    </svg>
    <span>Agree on LOI</span>
  </div>

  <div class="step step--lawyer">
    <div class="figure-placeholder" role="img" aria-label="Small dark silhouette of a lawyer in a suit"></div>
    <span>Send to Lawyer<br>to have first draft<br>of lease created<span class="step-note">1 week</span></span>
  </div>
</main>
</body>
</html>
```